Looking for a modern, Professional business card design

We have a simple business card, but are looking for a more modern, professional look. A sample of the basic card is attached as well as the logo. We would also like to add that we offer:
Struggling with your finances?
- Learn to become debt free
- Discover the power of cash
- Control your money instead of it controlling you
Let us help you achieve a new level of financial freedom!
Also, we would like to have a "SPECIAL OFFER!: FREE 30 minute consultation"
Financial Planning

```html
<!DOCTYPE html>
<html lang="en">
<head>
<meta charset="utf-8">
<title>Brightpath Money Coaching – Business Card</title>
<link rel="stylesheet" href="https://fonts.googleapis.com/css2?family=Roboto:ital,wght@0,400;0,500;0,700;1,700&display=swap">
<style>
  :root {
    --backdrop: #8f8f8f;
    --paper: #f1f1ef;
    --green-dark: #2f8a2f;
    --green-mid: #4aa437;
    --green-light: #8cc63f;
    --heading-green: #2b8e2f;
    --ink: #333333;
    --ink-strong: #111111;
    --white: #ffffff;
  }
  * { box-sizing: border-box; margin: 0; padding: 0; }
  html, body { width: 1105px; height: 1200px; overflow: hidden; }
  body {
    background: var(--backdrop);
    font-family: "Roboto", Arial, sans-serif;
    position: relative;
  }
  .card {
    position: absolute;
    left: 182px;
    width: 746px;
    height: 426px;
    background: var(--paper);
    overflow: hidden;
  }
  .card--front { top: 120px; }
  .card--back { top: 635px; }

  .front-band { position: absolute; inset: 0; width: 100%; height: 100%; }

  .brand {
    position: absolute;
    left: 40px;
    top: 70px;
    display: flex;
    align-items: center;
    gap: 14px;
  }
  .brand__dot {
    width: 34px; height: 34px; border-radius: 50%;
    background: var(--green-mid);
  }
  .brand__name {
    font-weight: 700;
    font-size: 30px;
    color: var(--green-dark);
    letter-spacing: 0.5px;
  }

  .contact {
    position: absolute;
    right: 38px;
    top: 210px;
    text-align: right;
    color: var(--white);
  }
  .contact__name { font-size: 26px; font-weight: 500; letter-spacing: 0.5px; }
  .contact__role { font-size: 20px; margin-top: 8px; }
  .contact__list { list-style: none; margin-top: 22px; font-size: 19px; }
  .contact__list li {
    display: flex; justify-content: flex-end; align-items: center;
    gap: 12px; height: 30px;
  }
  .contact__list svg { width: 18px; height: 18px; flex: none; }

  .offer-badge { position: absolute; left: 8px; top: 300px; width: 116px; height: 116px; }

  .back-brand {
    position: absolute;
    top: 92px; left: 0; right: 0;
    display: flex; justify-content: center; align-items: center; gap: 16px;
  }
  .back-brand__dot { width: 56px; height: 56px; border-radius: 50%; background: var(--green-mid); }
  .back-brand__name { font-size: 40px; font-weight: 700; color: var(--green-dark); letter-spacing: 1px; }

  .divider {
    position: absolute; left: 95px; right: 95px; top: 222px;
    height: 1px; background: #d6d6d6;
  }
  .pitch {
    position: absolute; top: 238px; left: 0; right: 0;
    text-align: center;
  }
  .pitch__heading { font-size: 21px; font-weight: 500; color: var(--heading-green); letter-spacing: 0.3px; }
  .pitch__line { font-size: 19px; color: var(--ink); margin-top: 6px; }
  .pitch__bullet {
    display: inline-block; width: 8px; height: 8px; border-radius: 50%;
    background: var(--green-mid); margin: 0 4px; vertical-align: middle;
  }
  .pitch__divider {
    margin: 14px auto 0; width: 556px; height: 1px; background: #dcdcdc;
  }
  .pitch__closing {
    margin-top: 18px; font-size: 19px; font-weight: 700; font-style: italic; color: var(--ink-strong);
  }
</style>
</head>
<body>

<section class="card card--front">
  <svg class="front-band" viewBox="0 0 746 426" preserveAspectRatio="none" aria-hidden="true">
    <defs>
      <radialGradient id="bandGlow" cx="0.45" cy="0.6" r="0.7">
        <stop offset="0" stop-color="#9bcc3c"/>
        <stop offset="0.55" stop-color="#58a935"/>
        <stop offset="1" stop-color="#2f8a2f"/>
      </radialGradient>
    </defs>
    <path d="M0 300 C 180 360, 420 120, 746 20 L 746 426 L 0 426 Z" fill="url(#bandGlow)"/>
    <path d="M0 300 C 180 360, 420 120, 746 20" fill="none" stroke="#2f8a2f" stroke-width="4"/>
  </svg>

  <div class="brand">
    <span class="brand__dot"></span>
    <span class="brand__name">BRIGHTPATH MONEY COACHING</span>
  </div>

  <div class="contact">
    <p class="contact__name">DANIEL R. HAYES</p>
    <p class="contact__role">Personal Financial Coach</p>
    <ul class="contact__list">
      <li>(555) 284-9017
        <svg viewBox="0 0 18 18" aria-hidden="true"><rect x="4" y="1" width="10" height="16" rx="2" fill="none" stroke="#fff" stroke-width="1.6"/><circle cx="9" cy="14" r="1" fill="#fff"/></svg>
      </li>
      <li>daniel@clearledgercoaching.com
        <svg viewBox="0 0 18 18" aria-hidden="true"><rect x="1" y="4" width="16" height="11" fill="#fff"/><path d="M1 4 L9 10 L17 4" fill="none" stroke="#4aa437" stroke-width="1.4"/></svg>
      </li>
      <li>www.clearledgercoaching.com
        <svg viewBox="0 0 18 18" aria-hidden="true"><circle cx="9" cy="9" r="7.5" fill="#fff"/><ellipse cx="9" cy="9" rx="3" ry="7.5" fill="none" stroke="#4aa437" stroke-width="1.2"/><line x1="1.5" y1="9" x2="16.5" y2="9" stroke="#4aa437" stroke-width="1.2"/></svg>
      </li>
    </ul>
  </div>

  <svg class="offer-badge" viewBox="0 0 116 116" role="img" aria-label="Special offer: free 30 minute consultation">
    <defs>
      <path id="badgeRing" d="M58 58 m-44 0 a44 44 0 1 1 88 0 a44 44 0 1 1 -88 0"/>
    </defs>
    <circle cx="58" cy="58" r="56" fill="#f4f6ef"/>
    <circle cx="58" cy="58" r="30" fill="#2f8a2f"/>
    <text font-family="Roboto, Arial, sans-serif" font-size="12.5" font-weight="700" fill="#2f8a2f" letter-spacing="0.6">
      <textPath href="#badgeRing">FREE 30 MINUTE CONSULTATION •</textPath>
    </text>
    <text x="58" y="55" text-anchor="middle" font-family="Roboto, Arial, sans-serif" font-size="11" font-weight="700" fill="#fff">SPECIAL</text>
    <text x="58" y="69" text-anchor="middle" font-family="Roboto, Arial, sans-serif" font-size="11" font-weight="700" fill="#fff">OFFER!</text>
  </svg>
</section>

<section class="card card--back">
  <div class="back-brand">
    <span class="back-brand__dot"></span>
    <span class="back-brand__name">BRIGHTPATH</span>
  </div>
  <div class="divider"></div>
  <div class="pitch">
    <h2 class="pitch__heading">STRUGGLING WITH YOUR FINANCES?</h2>
    <p class="pitch__line">Learn to become debt free<span class="pitch__bullet"></span>Discover the power of cash</p>
    <p class="pitch__line">Control your money instead of it controlling you</p>
    <div class="pitch__divider"></div>
    <p class="pitch__closing">Let us help you achieve a new level of financial freedom!</p>
  </div>
</section>

</body>
</html>
```